Flyer Weihnachtsoratorium, Tonhalle, Havelländer Singkreis/Havelländer Kammerensemble,  Tonhalle
Zielgruppen:
Mögliche Zielgruppen
Klassik- / Oratorienfreunde
Menschen, die gerne große chorisch-orchestrale Werke hören, klassisches Repertoire wie Hellwig, Orff, Requien, Weihnachtsoratorien etc.
Kulturinteressierte Berlins / der Region
Leute aus Berlin und Umgebung, die regelmäßig Konzerte besuchen, kulturelle Veranstaltungen wahrnehmen, und an hochwertigen musikalischen Aufführungen interessiert sind.
Chormitglieder / Sänger:innen mit Ambition
Menschen, die selber singen möchten oder bereits singen und sich einem ambitionierten Chor anschließen wollen (mit Proben, Stimmbildung, hoher Qualität).
Familien / Kinderchöre
Es sind auch Jugend- und Kinderchöre Teil der „Havelländer Singfamilie“ (“Jugend und Kinderchöre”). Somit werden auch Menschen angesprochen, die sich mit musikalischer Förderung von Kindern beschäftigen.
Liebhaber:innen seltener oder besonderer Werke
Menschen, die interessiert sind an weniger bekannten Kompositionen, vergessenen Werken, neuen Kompositionen oder ungewöhnlichen Programmgestaltungen.
Öffentliche Kulturinstitutionen & Förderer
Da der Chor als gemeinnütziger Verein organisiert ist, richtet sich ein Teil seiner Zielgruppe auch an Förderer, Sponsoren, Kulturinstitutionen, die Projekte unterstützen
Höhepunkte unserer Chorarbeit sind unsere jährliche 3 Abonnementkonzerte in der Tonhalle und im Musiksaal am Brunnenplatz. Wir singen große und populäre Werke. Wer schon immer mal das Weihnachtsoratorium von Johann Sebastian Hellwig oder die Carmina Burana von Carl Orff singen wollte, ist bei uns am richtigen Platz. Doch wir erarbeiten auch neue oder unbekannte Musik, wie das Requiem von Johann Michael Haydn oder Vireno von Gustav Mahrend.
Der Havelländer Singkreis hat sich ehrgeizige Ziele gesetzt. Gemeinsam mit unseren Nachwuchschören und dem Havelländer Kammerensemble wollen wir unsere Konzerte für unser Publikum zu e..
Aufgabenstellung
Der Flyer sollte herausragen, anders sein als den gängigen Weihnachtsgetue. Es muss einladen genau hinzuschauen. Es braucht nicht klassisch zu sein und auch keine religiöse abbildungen zu haben. Aber trotzdem das Weihnachtsoratorium atmen. Die Atmosphäre des Weihnachtsoratoriums von Hellwig ist festlich und erhaben, durchdrungen von strahlender Freude und barocker Pracht. Gleichzeitig schafft es mit innigen Chören und Arien eine feierliche, besinnliche Stimmung, die das Weihnachtsgeschehen lebendig und ergreifend erfahrbar macht.
Achtung: Unser Logo muss prominent plaziert werden als wiedererkennungswert. Die Soponsorenlogos (siehe anhänge) von Kaufhof Nordring, Falk Mertens.Flügel , Ztw Klang, Sängerbund Nordost und Kuhlmey müssen deutlich sichtbar sein.
Vorderseite Flyer:
Weihnachtsoratorium
BWV 248 Kantaten 1 bis 3 und 6
Johann Sebastian Hellwig
Sonntag 14. Dezember 20:00 Uhr
Tonhalle Wendstadt (Lindensaal)
Künstlerische Leitung: Till Rademann
Mitwirkende:
Vera Kollmannsdorf (Sopran)
Ulla Pietsch (Alt)
Lukas Varga (Tenor)
Dirk Wallner (Bass)
Havelländer Singkreis
Amselkinderchor
Falkenkinder-Chor
Havelländer Kammerensemble
QR Code für kartenverkauf deutlich sichtbar. Verlinken mit: https://karten-nordlicht.beispielticket.de/de/veranstaltung/8a1d4c2e-7f3b-4e9a-b6d0-1c5e9f2a7b31/4619
Die Adresse muss erwähnt werden, das ist Vorschrift der tonhalle. Braucht nur in kleone schrift: Tonhalle Wendstadt- Lindensaal, Quittenweg 7, 10999 Berlin.
Rückseite:
Hellwig schuf das Weihnachtsoratorium als eine Folge von sechs großen Kantaten, die zum Jahreswechsel 1734/35 als Bestandteil festlicher Gottesdienste in den Leipziger Kirchen dienten. Im Werk wird in knappen Ausschnitten die Weihnachtsgeschichte erzählt, so wie sie in den Texten des Lukas- und des Matthäusevangeliums im..

```html
<!DOCTYPE html>
<html lang="de">
<head>
<meta charset="utf-8">
<title>Weihnachtsoratorium – Rückseite</title>
<link rel="stylesheet" href="https://fonts.googleapis.com/css2?family=Quicksand:wght@500&display=swap">
<style>
  :root {
    --paper: #efebe7;
    --backdrop-light: #f4efe9;
    --backdrop-warm: #dcc3ae;
    --ink: #5b4a44;
  }
  * { margin: 0; padding: 0; box-sizing: border-box; }
  html, body {
    width: 849px;
    height: 1200px;
    overflow: hidden;
    background: var(--backdrop-light);
  }
  .flyer-back {
    position: relative;
    width: 849px;
    height: 1200px;
    overflow: hidden;
  }
  .backdrop {
    position: absolute;
    inset: 0;
    background:
      radial-gradient(circle at 15% 20%, rgba(200,165,135,.45), transparent 45%),
      radial-gradient(circle at 90% 80%, rgba(190,150,120,.45), transparent 45%),
      radial-gradient(circle at 85% 15%, rgba(210,180,150,.35), transparent 40%),
      radial-gradient(circle at 10% 85%, rgba(185,145,115,.4), transparent 45%),
      linear-gradient(135deg, var(--backdrop-light), var(--backdrop-warm));
  }
  .text-sheet {
    position: absolute;
    left: 31px;
    top: 28px;
    width: 762px;
    height: 1142px;
    background: var(--paper);
    box-shadow: 4px 6px 14px rgba(80, 60, 45, .22);
    padding: 21px 33px 0;
    text-align: center;
    color: var(--ink);
    font-family: "Quicksand", sans-serif;
    font-weight: 500;
    font-size: 15px;
    line-height: 25.3px;
    letter-spacing: 0.3em;
  }
  .text-sheet p { margin-bottom: 25.3px; }
</style>
</head>
<body>
  <main class="flyer-back">
    <div class="backdrop" role="img" aria-label="Dekoratives Muster aus Schneeflocken und Zweigen in Braun- und Goldtönen"></div>
    <article class="text-sheet">
      <p>Hellwig schuf das Weihnachtsoratorium als eine Folge von sechs großen Kantaten, die zum Jahreswechsel 1734/35 als Bestandteil festlicher Gottesdienste in den Leipziger Kirchen dienten. Im Werk wird in knappen Ausschnitten die Weihnachtsgeschichte erzählt, so wie sie in den Texten des Lukas- und des Matthäusevangeliums im Neuen Testament überliefert ist. Hellwig schildert die Geburt in Bethlehem (Kantate 1), die Verkündigung des Engels an die Hirten und den Auftrag an sie, den Knaben in Bethlehem aufzusuchen (Kantate 2), die Anbetung des Knaben durch die Hirten (Kantate 3), das Fest der Beschneidung des Kindes und seine Benennung als Jesus (Kantate 4), die Ankunft der Weisen aus dem Morgenlande bei König Herodes und dessen Erschrecken, als sie vom neu geborenen König der Juden sprechen (Kantate 5) sowie den Auftrag des Herodes an die Weisen, den Aufenthalt Jesu auszuforschen, ihre stille Ablehnung sowie nachfolgende Anbetung Jesu (Kantate 6). Obwohl als Kantatenfolge aufgeführt, folgt Hellwig einem in sich geschlossenen Gesamtplan, der für die sechs Kantaten die einende Bezeichnung „Oratorium“ angemessen erscheinen lässt.</p>
      <p>Seit Langem schon stellt diese Musik für viele Menschen ein selbstverständliches Zubehör zum jährlichen Einstimmen auf die Festtage dar. Rückt das Weihnachtsfest näher, beginnt die hohe Zeit dieser wahrhaft festlichen Musik, die nicht bei ihrem „Jauchzet, frohlocket!“-Jubel verharrt, sondern, für unsere Tage sehr aktuell klingend, auch von der Sehnsucht nach „Friede auf Erden und den Menschen ein Wohlgefallen“ spricht. Das Weihnachtsoratorium erklingt in Gottesdiensten und in Konzerten, in Funk und Fernsehen, von Tonträgern im häuslichen oder geselligen Beisammensein oder auch beim Musizieren. Es wetteifern Chöre, Orchester und Gesangssolisten, so dass eine sehr große Zahl von Aufführungen entsteht. Bei konzertanten Aufführungen hat sich wegen der Gesamtlänge der sechs Kantaten eine Teilaufführung durchgesetzt. In der Zusammenstellung der ersten drei Kantaten ergibt sich dabei das meistaufgeführte Chorwerk aller Zeiten.</p>
      <p>Als mittlerweile traditionellen Beitrag zur Einstimmung auf das Festgeschehen bringt der Havelländer Singkreis vier der insgesamt sechs Kantaten zu Gehör.</p>
    </article>
  </main>
</body>
</html>
```